Automotive component supplier needs a business card design

We need a business card design for our company called Velmar Global Components Ltd based in the UK. We are a supplier of interior and exterior components to premium car manufacturers such as Corvane Hale, Durrant Fyfe, Maxtorn and Valdessimo. We would like to see a modern business card design that uses the colour blue.

Target Market(s)

Premium automotive car manufacturers.

Industry/Entity Type

Automotive

Contact Information for Business Card

Company Name : Velmar Global Components Limited
Address: 17 Tamsey Yard, Upper Drisk, Warwick, CV31 8RJ, United Kingdom
Web Address : www.velmarparts-example.co.uk

Font styles to use
Other font styles liked:
• Helvetica

Colors
3176b5
0255a3
85acd3
cfdeed
cee9f5
85cae6
34a6d7
0692cd
9bcb3c

Requirements
Must have
• Clear company logo and a mixture of blue colours.
Nice to have
• A high quality modern image.
Should not have
• Multiple colours.

```html
<!DOCTYPE html>
<html lang="en">
<head>
<meta charset="utf-8">
<title>Velmar Global Components – Business Card</title>
<link rel="stylesheet" href="https://fonts.googleapis.com/css2?family=Roboto:wght@300;400;700;900&display=swap">
<style>
  :root {
    --brand-blue: #0692cd;
    --deep-blue: #0255a3;
    --accent-green: #9bcb3c;
    --card-white: #ffffff;
    --canvas-bg: #e9edf1;
    --rule-green: #cfe3a6;
  }
  html, body {
    margin: 0;
    padding: 0;
    width: 1200px;
    height: 1000px;
    overflow: hidden;
    background: var(--canvas-bg);
    font-family: "Roboto", Helvetica, Arial, sans-serif;
  }
  .canvas {
    position: relative;
    width: 1200px;
    height: 1000px;
  }
  .card {
    position: absolute;
    width: 640px;
    height: 370px;
    background: var(--card-white);
    box-shadow: 0 6px 18px rgba(0, 0, 0, 0.18);
  }
  .card svg { display: block; width: 100%; height: 100%; }
  .card--front { left: 70px; top: 80px; }
  .card--back { left: 490px; top: 550px; }

  .fill-blue { fill: var(--brand-blue); }
  .fill-green { fill: var(--accent-green); }
  .fill-white { fill: var(--card-white); }
  .stroke-white { stroke: var(--card-white); fill: none; stroke-width: 1.6; stroke-linecap: round; stroke-linejoin: round; }

  .brand-name {
    fill: var(--brand-blue);
    font-weight: 900;
    letter-spacing: 1px;
  }
  .brand-tag {
    fill: var(--brand-blue);
    font-weight: 300;
    letter-spacing: 0.5px;
  }
  .company-line {
    fill: var(--brand-blue);
    font-weight: 400;
  }
  .address-line {
    fill: var(--card-white);
    font-weight: 300;
  }
  .rule { stroke: var(--rule-green); stroke-width: 1.2; }
</style>
</head>
<body>
<main class="canvas">

  <section class="card card--front" aria-label="Business card front">
    <svg viewBox="0 0 640 370" xmlns="http://www.w3.org/2000/svg">
      <rect class="side-band fill-blue" x="0" y="0" width="34" height="220"/>
      <rect class="side-band fill-green" x="0" y="220" width="34" height="150"/>
      <path class="sweep fill-blue" d="M488 0 Q450 250 300 370 L640 370 L640 0 Z"/>

      <circle class="brand-dot fill-green" cx="80" cy="158" r="7"/>
      <text class="brand-name" x="96" y="178" font-size="62">VELMAR</text>
      <text class="brand-tag" x="98" y="204" font-size="15.5">GLOBAL COMPONENTS</text>
      <text class="company-line" x="98" y="226" font-size="13">Company Name : Velmar Global Components Limited</text>

      <text class="address-line" font-size="8.5" transform="translate(622 30) rotate(90)">Address: 17 Tamsey Yard, Upper Drisk, Warwick, CV31 8RJ</text>
    </svg>
  </section>

  <section class="card card--back" aria-label="Business card back">
    <svg viewBox="0 0 640 370" xmlns="http://www.w3.org/2000/svg">
      <rect class="side-band fill-green" x="606" y="0" width="34" height="150"/>
      <rect class="side-band fill-blue" x="606" y="150" width="34" height="220"/>
      <path class="sweep fill-blue" d="M0 0 Q60 300 330 370 L0 370 Z"/>

      <circle class="brand-dot fill-green" cx="218" cy="60" r="5"/>
      <text class="brand-name" x="230" y="74" font-size="38">VELMAR</text>
      <text class="brand-tag" x="231" y="91" font-size="10">GLOBAL COMPONENTS</text>
      <text class="company-line" x="231" y="104" font-size="7.5">Company Name : Velmar Global Components Limited</text>

      <line class="rule" x1="330" y1="150" x2="470" y2="150"/>

      <g class="contact-icons">
        <g class="icon icon--pin" transform="translate(360 180)">
          <circle class="fill-blue" r="11"/>
          <path class="stroke-white" d="M0 6 C-5 0 -5 -2 -5 -3 A5 5 0 0 1 5 -3 C5 -2 5 0 0 6 Z"/>
          <circle class="fill-white" cx="0" cy="-3" r="1.4"/>
        </g>
        <g class="icon icon--phone" transform="translate(392 180)">
          <circle class="fill-blue" r="11"/>
          <path class="stroke-white" d="M-4 -5 L-1 -5 L0 -2 L-2 -1 Q-1 2 2 3 L3 1 L6 2 L6 5 Q-5 6 -5 -4 Z"/>
        </g>
        <g class="icon icon--device" transform="translate(424 180)">
          <circle class="fill-blue" r="11"/>
          <rect class="stroke-white" x="-6" y="-4" width="12" height="8" rx="1.2"/>
        </g>
      </g>

      <text class="address-line" font-size="8.5" transform="translate(12 96) rotate(90)">Address: 17 Tamsey Yard, Upper Drisk, Warwick, CV31 8RJ</text>
    </svg>
  </section>

</main>
</body>
</html>
```